Flyer Design Project for Harbourline Janitorial Group Inc.

We require a double sided marketing flyer 8 1/2 x 11. The flyer will also be marketed via e-mail using one or both sides. "Outside of the box" but yet "professional" marketing is what we'd like to achieve.

Harbourline Janitorial Group Inc., is a building service company providing cleaning, caretaking and concierge service to residential/stratas (condominiums/apartments)...(These services are usually provided during daytime hours). and janitorial service to commercial buildings ( service provided at night time).

- 100% green cleaning chemicals and systems
- Professionally trained staff
- Customer service is #1 priority
- Excellent Communication systems

Brochure to be 2 pages.:

Side 1: marketing residential/strata building services with a focus on providing cleaning services with a sub-focus on caretaking and concierge. We also provide move-in/out service where we coordinate with tenants to arrange access to the building, elevators and provide security (no moving involved)

Side 2: marketing night time janitorial service to property managers, corporate head offices, small offices, industrial facilities

http://www.tidy-nest-example.com/index.php

http://www.brightkeepwest.example/services

These websites are from the best maid cleaning business and best strata//residential cleaning business in the city. The maid website is "you" focused, that works! The other is very straight forward and to the point, which also works.

At the end of the day our target audience ( property managers and building owners ) want us to take away one of their biggest headaches - "CLEANING". They have better things to be doing than dealing with whether or not the elevator is clean! That's our job! We're in the CLEANING business and when they don't hear a word from any of their tenants, we're doing our job and they're HAPPY :) WE TAKE AWAY HEADACHES AND MAKE PEOPLE HAPPY!

very multi-cultural target audience!

HOW CAN WE SHOW THEM IN A FLYER? THAT'S THE CHALLENGE! AND THE WINNING DESIGNER WILL BE THE ONE WHO CAN EFFECTIVELY COMMUNICATE THIS IN 1-2 PAGES.
Updates

Thank you all very much. Verolinda and Quill, your designs are very encouraging.

Design 1223617: The layout is close to what we are hoping to achieve as it may also be incorporated into a web site homepage with each block used as a link to more info. The pictures however, make it look like any other company flyer.

Design 1224020: Also a very good layout but again not liking the pictures.

Overall, some of the designs are a little to busy with information. I would like to see something just a little more simple and yet unique that stands out against other companies.

Look forward to the second round. Thank you all very much!

Please see the new files called commercial building pics, residential strata pics and misc pics that you can use in the brochure. These are the types of pictures I would like included. Thanks.

Hi Designers

Would like to see a design that combines the layout format of the bottom half of 1234602 ( easy to read) and the top half of 1227356 ( like the pictures in this one).

Also, want to replace "Marketing....." with Side #1 " Providing residential/stratas with quality, affordable cleaning, caretaking and concierge services.. and then the rest of the text in point/bullet form.

With side #2, want to replace " Marketing...." with "Providing quality, affordable commercial janitorial service to....

                                   

 

Please use latest pictures uploaded. The designs we've liked so far have 1 large picture ( picture of buildings ) on each side with 2-3 smaller pics in various layouts. i.e. for side 1 : Cleaning ( a picture of a cleaner ) Caretaking ( picture of handyman in white shaking hand) Concierge ( picture of person at a desk on the phone)

The font should be large and easy to read. We also like the designs where key points are in point form.

The company name and logo and contact info should be easy to read.

We did like one design using vector characters but think they should only be incorporated as part of the overall design

Target Market(s)

Property Managers, Building Owners, Multicultural Decision makers, aged 28 - 60, very busy people

Industry/Entity Type

Janitorial Service

Requirements
Must have
• 2 pages, 8 1/2 x 11 ( double sided) but can be used separately
Nice to have
• Would like to be able to change photos for different campaigns

```html
<!DOCTYPE html>
<html lang="en">
<head>
<meta charset="utf-8">
<title>Harbourline Janitorial Group Inc. – Flyer</title>
<link rel="stylesheet" href="https://fonts.googleapis.com/css2?family=Open+Sans:wght@400;600;700;800&display=swap">
<style>
  :root {
    --green: #7dc242;
    --green-dark: #5c9e2a;
    --green-light: #b6e07a;
    --ink: #2b2b2b;
    --grey: #555a5e;
    --frame: #c9cdd0;
    --paper: #ffffff;
    --sky: #5d8fb8;
    --sky-light: #cfe2ef;
    --floor: #c9cbc6;
    --floor-dark: #8d918c;
  }
  * { margin: 0; padding: 0; box-sizing: border-box; }
  html, body { width: 942px; height: 1200px; overflow: hidden; background: #ececec; }
  .flyer {
    position: relative; width: 942px; height: 1200px; overflow: hidden;
    background: var(--paper);
    font-family: "Open Sans", Arial, sans-serif;
  }
  .shapes { position: absolute; inset: 0; }
  .brand {
    position: absolute; left: 480px; top: 168px; width: 440px; text-align: center;
    font-size: 66px; font-weight: 600; color: var(--ink); letter-spacing: -1px;
  }
  .services-head { position: absolute; font-weight: 800; color: var(--grey); font-size: 31px; letter-spacing: 0.5px; }
  .services-head.cleaning { left: 407px; top: 330px; }
  .services-head.caretaking { left: 340px; top: 368px; }
  .services-head.concierge { left: 269px; top: 406px; }
  .point {
    position: absolute; color: #fff; font-weight: 700; font-size: 15px; line-height: 1.2;
    text-transform: uppercase;
  }
  .point .sub { text-transform: none; }
  .service-title { position: absolute; left: 208px; top: 790px; font-size: 38px; font-weight: 800; color: var(--grey); }
  .service-line { position: absolute; font-size: 20px; color: var(--green-dark); white-space: nowrap; }
  .move-note { position: absolute; left: 186px; top: 1036px; font-size: 17px; font-weight: 800; color: var(--ink); line-height: 1.4; }
  .contact { position: absolute; right: 24px; top: 1040px; text-align: right; color: #fff; }
  .contact .company { font-size: 23px; font-weight: 600; }
  .contact .address { font-size: 14px; line-height: 1.7; margin: 4px 30px 4px 0; }
  .contact .phone { font-size: 25px; font-weight: 700; }
  .contact .email { font-size: 21px; font-weight: 600; margin-top: 4px; }
</style>
</head>
<body>
<main class="flyer">
  <svg class="shapes" width="942" height="1200" viewBox="0 0 942 1200">
    <defs>
      <linearGradient id="sky" x1="0" y1="0" x2="1" y2="1">
        <stop offset="0" stop-color="var(--sky-light)"/>
        <stop offset="1" stop-color="var(--sky)"/>
      </linearGradient>
      <linearGradient id="floor" x1="0" y1="0" x2="0" y2="1">
        <stop offset="0" stop-color="#e9ebe6"/>
        <stop offset="0.5" stop-color="var(--floor-dark)"/>
        <stop offset="1" stop-color="var(--floor)"/>
      </linearGradient>
      <radialGradient id="tile-green" cx="0.5" cy="0.5" r="0.7">
        <stop offset="0" stop-color="var(--green-light)"/>
        <stop offset="1" stop-color="var(--green-dark)"/>
      </radialGradient>
      <linearGradient id="panel" x1="0" y1="0" x2="1" y2="1">
        <stop offset="0" stop-color="var(--green)"/>
        <stop offset="1" stop-color="var(--green-dark)"/>
      </linearGradient>
    </defs>

    <polygon points="0,0 262,0 0,152" fill="var(--green)"/>

    <g class="tile" transform="translate(0 545) rotate(35)">
      <rect x="-80" y="-80" width="160" height="160" rx="12" fill="#f4f5f6" stroke="var(--frame)" stroke-width="9"/>
    </g>
    <g class="tile" transform="translate(55 755) rotate(30)" role="img" aria-label="Green decorative tile with swirl motif">
      <rect x="-75" y="-75" width="150" height="150" rx="12" fill="url(#tile-green)" stroke="var(--frame)" stroke-width="8"/>
    </g>
    <g class="tile" transform="translate(0 1085) rotate(28)">
      <rect x="-60" y="-60" width="120" height="120" rx="10" fill="url(#tile-green)" stroke="var(--frame)" stroke-width="8"/>
    </g>
    <g class="tile" transform="translate(70 1215) rotate(28)">
      <rect x="-55" y="-55" width="110" height="110" rx="10" fill="url(#tile-green)" stroke="var(--frame)" stroke-width="8"/>
    </g>
    <g class="tile" transform="translate(935 890) rotate(30)">
      <rect x="-70" y="-70" width="140" height="140" rx="10" fill="#f4f5f6" stroke="var(--frame)" stroke-width="8"/>
    </g>

    <g transform="translate(235 200) rotate(40)" role="img" aria-label="Photo of a tall glass office tower against a blue sky">
      <rect x="-150" y="-150" width="300" height="300" rx="14" fill="url(#sky)" stroke="#fff" stroke-width="4"/>
    </g>

    <polygon points="455,265 942,265 942,297 470,297 480,281" fill="var(--green)"/>

    <g transform="translate(740 575) rotate(40)" role="img" aria-label="Photo of a freshly mopped cafeteria floor with a yellow mop bucket and wet-floor sign">
      <rect x="-195" y="-195" width="390" height="390" rx="16" fill="url(#floor)" stroke="#fff" stroke-width="4"/>
    </g>

    <g fill="var(--green)" style="filter: drop-shadow(3px 4px 3px rgba(0,0,0,0.35))">
      <polygon points="48,464 446,464 436,507 35,507"/>
      <polygon points="76,521 481,521 471,577 63,577"/>
      <polygon points="112,586 516,586 506,634 99,634"/>
      <polygon points="150,643 557,643 547,695 137,695"/>
      <polygon points="186,710 595,710 585,759 173,759"/>
    </g>

    <g transform="translate(790 1080) rotate(-28)">
      <rect x="-260" y="-190" width="560" height="400" rx="26" fill="url(#panel)" stroke="var(--frame)" stroke-width="10"/>
    </g>
  </svg>

  <div class="brand">Harbourline</div>

  <div class="services-head cleaning">CLEANING</div>
  <div class="services-head caretaking">CARETAKING</div>
  <div class="services-head concierge">CONCIERGE</div>

  <div class="point" style="left:58px;top:468px;"># 1 Priority - Customer Service<br><span class="sub">&nbsp;&nbsp;And communication</span></div>
  <div class="point" style="left:96px;top:527px;">Over 20 years industry experience<br>Trained, couteous staff</div>
  <div class="point" style="left:160px;top:600px;">100% Green Chemicals</div>
  <div class="point" style="left:195px;top:648px;"><span class="sub">Servicing greater vancouver</span><br>Affordable, quality service</div>
  <div class="point" style="left:240px;top:714px;">New construction?<br>&nbsp;&nbsp;&nbsp;&nbsp;&nbsp;&nbsp;&nbsp;&nbsp;&nbsp;&nbsp;&nbsp;&nbsp;We do move-ins/oust</div>

  <div class="service-title">Service</div>
  <div class="service-line" style="left:242px;top:842px;">Daily, weekly, monthly and yearly cleaning services</div>
  <div class="service-line" style="left:210px;top:870px;">Initial cleaning / one-time jobs</div>
  <div class="service-line" style="left:165px;top:898px;">Project work / all types of floor maintenance</div>
  <div class="service-line" style="left:124px;top:925px;">Caretaker and building management services</div>
  <div class="service-line" style="left:96px;top:953px;">Monthly building reports and audits</div>

  <div class="move-note">NEW CONSTRUCTION?<br>WE DO MOVE-INS/OUTS</div>

  <div class="contact">
    <div class="company">Harbourline Janitorial Group Inc.</div>
    <div class="address">1234, street Name, State Name,<br>Country Name, Country Name,</div>
    <div class="phone">CALL 604-555-0142</div>
    <div class="email">E: dana@harbourline.example</div>
  </div>
</main>
</body>
</html>
```